International Dental Education Website

This project is for a small teaching center on endodontic and micro dentistry in Norway. We need a Wordpress website design to display and highlight dental educational courses. Please use our new logo - see attached file. We like lighter, pastel oriented colors. The following sites are nicely laid out and you can use these as a guideline of sorts but I do want a unique site.
http://vorelta.nl/en, http://www.trasmolin.com/Education.aspx?currentSection=courses&cid=14,
http://www.kapiverno.com/.
Please create a space for a possible video on the home page. Please include a small contact form on the home page(name, email, phone, text box). Would like a horizonatal naviagtion bar. Would like an image to go across the whole top part of the site and this may rotate. Please use a stock image that shows a classroom type setting. Put phone number at the top of the screen. Put address and sitemap in a footer.

Reason: Upcoming vacation with limited internet access. Please continue to submit any designs. Thanks you.

Reason: The client is from a foreign country and is on an extended vacation.

Target Market(s)

General dentists (GPs) and specialists in Endodontics

Industry/Entity Type

Dental

Requirements
Must have
• Sitemap: HOME, COURSES, LECTURER, CONTACT US,
NORWEGIAN/ENGLISH. Phone number is: +47 93516072. Business name and address: Vatu Lok AS, Endodontic Teaching Center,
Solbergs vei 14C, 0291 Oslo, Norway.

```html
<!DOCTYPE html>
<html lang="en">
<head>
<meta charset="utf-8">
<title>Vatu Lok – Endodontic Teaching Center</title>
<link rel="stylesheet" href="https://fonts.googleapis.com/css2?family=Oswald:wght@300;400&family=Arimo:wght@400;700&display=swap">
<style>
:root{
  --teal:#4fb3b8;
  --teal-dark:#2e8e94;
  --teal-soft:#85d0d4;
  --aqua-bg:#e6fbfd;
  --field:#dcfafd;
  --field-line:#8fcbd0;
  --grey-text:#6b6b6b;
  --ink:#111;
  --frame:#b9c4c6;
  --white:#fff;
}
*{box-sizing:border-box;margin:0;padding:0}
html,body{width:1139px;height:1200px;overflow:hidden;background:var(--white)}
body{position:relative;font-family:"Arimo",Arial,sans-serif;color:var(--ink)}
.abs{position:absolute}
.heading{font-family:"Oswald",sans-serif;font-weight:300;letter-spacing:-.3px}

/* top bar */
.lang-box{left:907px;top:0;width:136px;height:52px;background:linear-gradient(#f3f3f3,#e4e4e4);border-radius:0 0 6px 6px;text-align:center;padding-top:6px}
.lang{font-size:13px;color:var(--grey-text)}
.lang .active{color:var(--teal)}
.phone{font-size:15px;color:var(--teal);margin-top:2px}

.arch{left:280px;top:36px}
.brand{left:470px;top:52px;width:200px;text-align:center;font-size:34px;color:var(--teal);font-weight:400;line-height:1}
.nav a{position:absolute;top:92px;font-family:"Oswald",sans-serif;font-weight:300;font-size:15px;color:#555;text-decoration:none}
.nav .current::after{content:"";position:absolute;left:50%;bottom:-9px;margin-left:-6px;border:6px solid transparent;border-bottom-color:var(--teal)}

/* hero */
.hero{left:94px;top:116px;width:951px;height:361px;border:1px solid var(--teal-soft)}
.hero-photo{position:absolute;left:0;top:0;width:100%;height:324px;background:linear-gradient(160deg,#8a8679 0%,#c5b8a6 40%,#b9a58e 65%,#6e6a61 100%)}
.hero-band{position:absolute;left:0;top:324px;width:100%;height:36px;background:var(--teal-soft)}
.hero-tag{position:absolute;left:0;top:324px;height:36px;width:280px;background:#9aa2a4;clip-path:polygon(0 0,100% 0,88% 100%,0 100%)}
.tooth-dot{position:absolute;left:8px;top:329px;width:29px;height:29px;border-radius:50%;background:#111;border:2px solid #fff}
.hero-tag-text{position:absolute;left:46px;top:329px;font-size:19px;color:#fff}
.hero-title{position:absolute;right:14px;top:326px;font-size:27px;color:var(--teal-dark)}
.hero-shadow{left:110px;top:477px;width:920px;height:18px;background:radial-gradient(ellipse at top,rgba(0,0,0,.35),rgba(0,0,0,0) 70%)}

.tagline{left:0;width:1139px;top:490px;text-align:center;font-size:38px;color:var(--teal);font-weight:300}

/* intro box */
.intro{left:93px;top:546px;width:952px;height:263px;border:1px solid var(--frame);background:var(--aqua-bg)}
.video{position:absolute;left:7px;top:7px;width:413px;height:248px;background:linear-gradient(135deg,#2f4fb0,#d5a14a 55%,#6c6c6c);}
.video-play{position:absolute;left:178px;top:95px;width:56px;height:38px;border-radius:9px;background:#1b1b1b}
.video-play::after{content:"";position:absolute;left:22px;top:11px;border-left:15px solid #fff;border-top:8px solid transparent;border-bottom:8px solid transparent}
.video-bar{position:absolute;left:0;bottom:0;width:100%;height:22px;background:#1c1c1c;border-top:3px solid #c0151a}
.copy{position:absolute;font-size:11.5px;line-height:14px;text-align:justify}
.copy p+p{margin-top:14px}
.section-title{position:absolute;font-size:20px;color:var(--teal-dark);white-space:nowrap}
.intro .section-title{left:446px;top:4px;width:496px;border-bottom:1px solid #9bb;padding-bottom:2px}
.intro .copy{left:446px;top:38px;width:498px;font-size:10.8px;line-height:13.5px}
.intro .copy p+p{margin-top:13px}

/* lower box */
.lower{left:93px;top:838px;width:952px;height:276px;border:1px solid var(--frame)}
.lower-panel{position:absolute;left:0;top:0;width:678px;height:100%;background:linear-gradient(90deg,#fff 70%,#e9ecec)}
.lower-strip{position:absolute;left:8px;top:8px;width:520px;height:55px;background:linear-gradient(90deg,#cfd3d4,#f4f4f4 90%,#fff)}
.lower-thumb{position:absolute;left:8px;top:8px;width:93px;height:55px;background:linear-gradient(135deg,#8d9596,#e3e5e5 60%,#c7a5a5)}
.lower .section-title{left:112px;top:20px}
.lower .copy{left:11px;top:79px;width:661px}

.form-title{position:absolute;left:700px;width:246px;text-align:center;font-size:15px;color:var(--teal)}
.form-sub{color:#777;font-size:14px}
.form-rule{position:absolute;left:740px;top:53px;width:170px;height:1px;background:linear-gradient(90deg,transparent,#9cc,transparent)}
.field{position:absolute;left:712px;width:201px;height:22px;background:var(--field);border:1px solid var(--field-line);border-radius:3px;font-size:10px;color:#777;padding:4px 6px;letter-spacing:.5px}
.submit{position:absolute;left:779px;top:240px;width:76px;height:22px;background:linear-gradient(#4fb8bf,#21868d);color:#fff;font-size:10px;font-weight:700;text-align:center;line-height:22px;border-radius:2px;box-shadow:0 6px 6px -4px rgba(0,0,0,.5)}

/* footer */
.footer{left:88px;top:1137px;width:955px;height:63px;background:var(--teal-soft);border-radius:8px 8px 0 0;overflow:hidden}
.footer-brand{position:absolute;left:0;top:0;width:175px;height:63px;background:#a5dde0;clip-path:polygon(0 0,80% 0,100% 50%,80% 100%,0 100%)}
.footer-brand span{position:absolute;left:20px;top:10px;font-size:26px;color:var(--teal-dark)}
.footer-address{position:absolute;left:180px;top:24px;font-size:10.5px;font-weight:700;color:#fff}
.footer-divider{position:absolute;left:794px;top:6px;width:1px;height:57px;background:#fff;opacity:.7}
.footer-link{position:absolute;top:10px;width:60px;text-align:center;font-size:10px;font-weight:700;color:#fff}
.footer-link i{display:block;margin:0 auto 3px;width:28px;height:28px;border-radius:50%;background:var(--teal);border:2px solid #d8f3f4}
</style>
</head>
<body>

<div class="abs lang-box heading">
  <div class="lang">NORWEGIAN / <span class="active">ENGLISH</span></div>
  <div class="phone">CALL US : +47 93516072</div>
</div>

<svg class="abs arch" width="575" height="82" viewBox="0 0 575 82" aria-hidden="true">
  <defs><linearGradient id="archFill" x1="0" x2="0" y1="0" y2="1"><stop offset="0" stop-color="#fff"/><stop offset="1" stop-color="#e2e2e2"/></linearGradient></defs>
  <path d="M0 82 C90 20 200 4 288 4 C376 4 486 20 575 82 Z" fill="url(#archFill)"/>
  <path d="M0 82 C70 38 130 22 190 14 C120 30 60 52 22 82 Z" fill="#6ec7cc"/>
  <path d="M575 82 C505 38 445 22 385 14 C455 30 515 52 553 82 Z" fill="#6ec7cc"/>
</svg>
<div class="abs brand heading">Vatu Lok</div>

<nav class="nav">
  <a class="current" style="left:133px">HOME</a>
  <a style="left:205px">COURSES</a>
  <a style="left:868px">LECTURER</a>
  <a style="left:953px">CONTACT US</a>
</nav>

<section class="abs hero">
  <div class="hero-photo" role="img" aria-label="Stock photo of a lecturer speaking to dental students in a tiered classroom"></div>
  <div class="hero-band"></div>
  <div class="hero-tag"></div>
  <div class="tooth-dot"></div>
  <div class="hero-tag-text heading">DENTAL EDUCATIONAL COURSES</div>
  <div class="hero-title heading">ENDODONTIC TEACHING CENTER</div>
</section>
<div class="abs hero-shadow"></div>

<h1 class="abs tagline heading">YOUR SOURCE FOR ENDODONTIC EDUCATION</h1>

<section class="abs intro">
  <div class="video" role="img" aria-label="Embedded video of a presenter introducing a dental product">
    <div class="video-play"></div>
    <div class="video-bar"></div>
  </div>
  <h2 class="section-title heading">ENDODONTIC TEACHING CENTER &nbsp;DENTAL EDUCATION COURSES</h2>
  <div class="copy">
    <p>VORELTA is an ultra modern centre of dental excellence which offers the very latest in innovative dental education courses. VORELTA is located in an elegant townhouse with a modern interior which exudes a calm atmosphere. It is the ideal surrounding to share knowledge and explore and develop new practical competencies.</p>
    <p>We at VORELTA are convinced you will feel at home while we guide you to efficiently build effective new competencies and ideas which will contribute to perfecting your own practice execution.</p>
    <p>VORELTA is an ultra modern centre of dental excellence which offers the very latest in innovative dental education courses. VORELTA is located in an elegant townhouse with a modern interior which exudes a calm atmosphere. It is the ideal surrounding to share knowledge and explore and develop new practical competencies.</p>
    <p>We at VORELTA are convinced you will feel at home while we guide you to efficiently build effective new competencies and ideas which will contribute to perfecting your own practice execution.</p>
  </div>
</section>

<section class="abs lower">
  <div class="lower-panel"></div>
  <div class="lower-strip"></div>
  <div class="lower-thumb" role="img" aria-label="Close-up photo of a dental model with teeth"></div>
  <h2 class="section-title heading">ENDODONTIC TEACHING CENTER &nbsp;DENTAL EDUCATION COURSES</h2>
  <div class="copy">
    <p>VORELTA is an ultra modern centre of dental excellence which offers the very latest in innovative dental education courses. VORELTA is located in an elegant townhouse with a modern interior which exudes a calm atmosphere. It is the ideal surrounding to share knowledge and explore and develop new practical competencies.</p>
    <p>We at VORELTA are convinced you will feel at home while we guide you to efficiently build effective new competencies and ideas which will contribute to perfecting your own practice execution.</p>
    <p>VORELTA is an ultra modern centre of dental excellence which offers the very latest in innovative dental education courses. VORELTA is located in an elegant townhouse with a modern interior which exudes a calm atmosphere. It is the ideal surrounding to share knowledge and explore and develop new practical competencies.</p>
    <p>We at VORELTA are convinced you will feel at home while we guide you to efficiently build effective new competencies and ideas which will contribute to perfecting your own practice execution.</p>
  </div>

  <div class="form-title heading" style="top:6px">WE LOOK FORWARD TO WELCOMING YOU!<br><span class="form-sub">MESSAGE US YOUR QUESTIONS</span></div>
  <div class="form-rule"></div>
  <div class="field" style="top:60px">Name</div>
  <div class="field" style="top:89px">Email</div>
  <div class="field" style="top:118px">Phone / Mobile</div>
  <div class="field" style="top:146px;height:83px">Message</div>
  <div class="submit">SUBMIT</div>
</section>

<footer class="abs footer">
  <div class="footer-brand"><span class="heading">Vatu Lok</span></div>
  <div class="footer-address">Vatu Lok AS, Endodontic Teaching Center, Solbergs vei 14C, 0291 Oslo, Norway.</div>
  <div class="footer-divider"></div>
  <div class="footer-link" style="left:818px"><i></i>Join us</div>
  <div class="footer-link" style="left:893px"><i></i>Sitemap</div>
</footer>

</body>
</html>
```